Yard Sign Design Needed

Yard sign needed for mowing & landscaping company. Would like to use the top logo with black background which is attached. Would like MOWING to be in large standout letters. The word "landscaping" can be smaller and more artistic or omitted. Will need room for phone number once design is approved. The phone number will need to stand out and look identical/similar to the word 'MOWING"

```html
<!DOCTYPE html>
<html lang="en">
<head>
<meta charset="utf-8">
<title>Talbrook Contractors – Mowing Yard Sign</title>
<link rel="stylesheet" href="https://fonts.googleapis.com/css2?family=Michroma&family=Orbitron:wght@900&display=swap">
<style>
  :root {
    --page-bg: #e9e9e6;
    --sign-black: #000000;
    --lime-light: #d3ec6a;
    --lime: #b3d136;
    --lime-deep: #8aae25;
    --olive: #8ea832;
    --white: #ffffff;
    --ink: #0a0a0a;
  }
  html, body {
    margin: 0;
    padding: 0;
    width: 750px;
    height: 1200px;
    overflow: hidden;
    background: var(--page-bg);
  }
  .yard-sign {
    position: absolute;
    left: 20px;
    top: 334px;
    width: 710px;
    height: 532px;
    background: var(--sign-black);
    overflow: hidden;
    white-space: nowrap;
    color: var(--white);
  }
  .brand {
    position: absolute;
    left: 0;
    right: 0;
    top: 40px;
    display: flex;
    flex-direction: column;
    align-items: center;
    font-family: "Michroma", sans-serif;
    color: var(--olive);
  }
  .brand-square {
    width: 70px;
    height: 70px;
    background: var(--olive);
    margin-bottom: 18px;
  }
  .brand-name {
    font-size: 30px;
    line-height: 34px;
    letter-spacing: 1px;
  }
  .brand-sub {
    font-size: 13px;
    line-height: 18px;
    letter-spacing: 1px;
  }
  .headline {
    position: absolute;
    left: 0;
    right: 0;
    top: 240px;
    text-align: center;
    font-family: "Orbitron", sans-serif;
    font-weight: 900;
    font-size: 104px;
    line-height: 112px;
    letter-spacing: -2px;
    background: linear-gradient(to bottom, var(--lime-light) 0%, var(--lime) 55%, var(--lime-deep) 100%);
    -webkit-background-clip: text;
    background-clip: text;
    color: transparent;
  }
  .subhead {
    position: absolute;
    left: 0;
    right: 0;
    top: 356px;
    text-align: center;
    font-family: "Michroma", sans-serif;
    font-size: 26px;
    line-height: 32px;
    letter-spacing: 30px;
    padding-left: 30px;
    color: var(--white);
  }
  .phone-pill {
    position: absolute;
    left: 53px;
    top: 418px;
    width: 599px;
    height: 83px;
    box-sizing: border-box;
    border: 3px solid var(--white);
    border-radius: 42px;
    background: linear-gradient(to bottom, var(--lime-light) 0%, var(--lime) 50%, var(--lime) 100%);
    display: flex;
    align-items: center;
  }
  .phone-icon {
    width: 58px;
    height: 58px;
    margin-left: 11px;
    flex: none;
  }
  .phone-number {
    margin-left: 22px;
    font-family: "Michroma", sans-serif;
    font-size: 41px;
    line-height: 1;
    color: var(--ink);
    letter-spacing: -1px;
  }
</style>
</head>
<body>
  <main class="yard-sign">
    <div class="brand">
      <div class="brand-square"></div>
      <div class="brand-name">TALBROOK</div>
      <div class="brand-sub">CONTRACTORS LLC</div>
    </div>

    <h1 class="headline" style="margin:0;">MOWING</h1>
    <p class="subhead" style="margin:0;">LANDSCAPING</p>

    <div class="phone-pill">
      <svg class="phone-icon" viewBox="0 0 58 58" aria-hidden="true">
        <circle cx="29" cy="29" r="27" fill="#000" stroke="#fff" stroke-width="2"/>
        <path d="M20 15 l6 7 -3 4 c2 4 5 7 9 9 l4 -3 7 6 -4 5 c-11 -1 -21 -11 -22 -22 z" fill="#fff"/>
      </svg>
      <span class="phone-number">5126-304-987</span>
    </div>
  </main>
</body>
</html>
```